We are full service plumbing contractors that are capable of performing all of your plumbing need...

A clean, crisp website that conveys we can handle any plumbing from drain cleaning, repairs, to new construction. But emphasis on Leak detection, under-slab and underground water service leaks, repairs, and reroutes. Leak detection by acoustical, Thermal, or tracer gas , methods.Also emphasize advanced drain cleaning technologies and equipment. Don't just poke ahole in the drain blockage, Clean the pipe, with our High pressure hydrojetters, or Chain knocker drain cables that expand to the width of the pipe being cleaned.

Number of Pages Required

5+ page

Font styles to use
Sans Serif

Requirements
Should not have
• Canned photos

```html
<!DOCTYPE html>
<html lang="en">
<head>
<meta charset="utf-8">
<title>ClearFlow Plumbing</title>
<link href="https://fonts.googleapis.com/css2?family=Oswald:wght@500;700&family=Open+Sans:wght@400;600;700&display=swap" rel="stylesheet">
<style>
:root{
  --navy:#0d3f86;
  --blue:#1c5db8;
  --sky:#3f86d6;
  --red:#e0201f;
  --dark:#2b2b2b;
  --ink:#333;
  --muted:#777;
  --light:#f1f1f1;
  --white:#fff;
  --yellow:#f4c430;
}
*{margin:0;padding:0;box-sizing:border-box}
html,body{width:1200px;height:2236px;overflow:hidden}
body{font-family:"Open Sans",Arial,sans-serif;color:var(--ink);background:var(--white);position:relative}
.abs{position:absolute}
.header{left:0;top:0;width:1200px;height:144px;background:linear-gradient(180deg,#0b3575,var(--blue))}
.brand{left:268px;top:26px;display:flex;align-items:center;gap:10px;color:var(--white);font-weight:700;font-size:26px}
.brand-dot{width:34px;height:34px;border-radius:50%;background:var(--red)}
.call{left:540px;top:30px;width:400px;text-align:right;white-space:nowrap;color:var(--white);font-family:"Oswald",sans-serif;font-weight:700;font-size:36px;line-height:44px;letter-spacing:1px}
.nav{left:262px;top:110px;width:676px;height:30px;background:var(--white);border-radius:4px;display:flex;align-items:center;padding:0 8px;gap:4px}
.nav a{font-size:10px;font-weight:600;color:#555;text-decoration:none;padding:7px 14px;border-right:1px solid #ddd}
.nav a.active{background:var(--red);color:var(--white);border-radius:3px}
.hero{left:0;top:144px;width:1200px;height:416px;background:linear-gradient(180deg,#2f6fbf,#1d4f97 60%,#143f7e)}
.hero-photo{left:0;top:144px;width:1200px;height:416px;background:linear-gradient(120deg,rgba(90,120,90,.45),rgba(40,90,160,.2) 50%,rgba(20,50,110,.4))}
.hero-title{left:276px;top:160px;color:var(--white);font-family:"Oswald",sans-serif;font-weight:700;font-size:42px;line-height:1.05;letter-spacing:1px}
.hero-circle{left:430px;top:270px;width:250px;height:250px;border-radius:50%;border:6px solid rgba(255,255,255,.8);background:radial-gradient(circle at 40% 40%,#8a9a6a,#4f6a44 60%,#3a4a3a)}
.contact{left:820px;top:170px;width:240px;color:var(--white)}
.contact h3{font-family:"Oswald",sans-serif;font-size:24px;font-weight:500}
.contact p{font-size:12px}
.contact .tel{color:var(--red);font-family:"Oswald",sans-serif;font-weight:700;font-size:28px;margin:2px 0 10px}
.field{height:28px;background:rgba(255,255,255,.25);border:1px solid rgba(255,255,255,.5);margin-bottom:8px;font-size:11px;padding:6px 8px}
.field.msg{height:80px}
.btn{display:inline-block;background:var(--red);color:var(--white);font-size:11px;font-weight:700;padding:8px 18px;border-radius:2px;white-space:nowrap}
.contact .btn{float:right;font-size:14px;padding:8px 22px}
.services{left:268px;top:620px;width:672px;display:flex;gap:12px}
.card{width:216px}
.card .ph{height:120px;background:linear-gradient(135deg,#8e8a80,#5a5650)}
.card h4{font-size:18px;font-weight:700;color:var(--dark);margin:10px 0 6px}
.card p{font-size:11px;line-height:1.45;color:var(--muted);height:72px}
.card .btn{margin-left:60px}
.video{left:0;top:912px;width:1200px;height:290px;background:linear-gradient(90deg,#3a3a3a,#6b6b6b 50%,#3a3a3a)}
.player{left:380px;top:928px;width:440px;height:258px;background:linear-gradient(135deg,#9a9386,#5e5a52)}
.bar{left:380px;top:1156px;width:440px;height:30px;background:rgba(0,0,0,.65)}
.arrow{top:1040px;color:var(--white);font-size:40px}
.about-ph{left:268px;top:1236px;width:204px;height:140px;background:linear-gradient(135deg,#e8ecef,#9aa3aa)}
.about{left:500px;top:1230px;width:440px}
.about h2{font-family:"Oswald",sans-serif;font-size:34px;color:var(--dark);font-weight:700}
.about p{font-size:11px;line-height:1.5;color:var(--muted);margin:8px 0 12px}
.testi{left:0;top:1440px;width:1200px;height:400px;background:var(--light)}
.testi h2{position:absolute;top:48px;width:1200px;text-align:center;font-family:"Oswald",sans-serif;font-size:32px;color:var(--dark)}
.testi .sub{position:absolute;top:96px;width:1200px;text-align:center;font-size:11px;color:var(--muted)}
.quote{top:1564px;width:270px;height:130px;background:var(--white);border-top:3px solid var(--red);padding:14px;font-size:11px;line-height:1.5;color:var(--muted)}
.avatar{top:1724px;width:56px;height:56px;border-radius:50%;background:#c9c9c9}
.who{top:1788px;width:200px;text-align:center;font-size:13px;font-weight:700;color:var(--dark)}
.who span{display:block;font-size:10px;font-weight:400;color:var(--muted)}
.round{top:1616px;width:26px;height:26px;border-radius:50%;background:#ccc;color:var(--white);text-align:center;line-height:26px;font-size:14px}
.cta{left:0;top:1972px;width:1200px;height:70px;background:var(--red)}
.cta-text{left:392px;top:1997px;white-space:nowrap;color:var(--white);font-size:12px;line-height:20px;font-weight:600}
.cta .btn{position:absolute;left:790px;top:20px;background:var(--white);color:var(--red)}
.figure{left:268px;top:1870px;width:110px;height:172px;background:linear-gradient(180deg,#9aa8c0,#3b5a90);border-radius:50px 50px 0 0}
.footer{left:0;top:2042px;width:1200px;height:150px;background:var(--dark)}
.fcol{top:2058px;width:200px;color:#bbb;font-size:10px;line-height:1.75}
.fcol h5{color:var(--white);font-size:11px;margin-bottom:4px}
.copy{left:0;top:2192px;width:1200px;height:44px;background:#1e1e1e;color:#999;font-size:10px;text-align:center;line-height:44px}
</style>
</head>
<body>
<div class="abs header"></div>
<div class="abs brand"><span class="brand-dot"></span>ClearFlow</div>
<div class="abs call">CALL 555.014.2290</div>
<nav class="abs nav"><a class="active">HOME</a><a>SERVICES</a><a>INDUSTRIES</a><a>ABOUT US</a><a>LOCATIONS</a><a>BLOG</a><a>CONTACT US</a></nav>

<div class="abs hero"></div>
<div class="abs hero-photo" role="img" aria-label="Plumber working on a yard pipe dig behind a house"></div>
<div class="abs hero-title">RAPLACE THE PIPE<br>WITHOUT MESS</div>
<div class="abs hero-circle" role="img" aria-label="Trenchless pipe replacement equipment in a lawn"></div>
<form class="abs contact">
  <h3>CONTACT US ONLINE</h3>
  <p>Or call us 24/7 for service</p>
  <div class="tel">555.014.2290</div>
  <div class="field">Name</div>
  <div class="field">Email</div>
  <div class="field">Phone</div>
  <div class="field msg">Message</div>
  <span class="btn">SUBMIT</span>
</form>

<section class="abs services">
  <div class="card"><div class="ph" role="img" aria-label="Residential plumbing work"></div><h4>Residential Services</h4><p>Leak detection, slab leak repair, repiping and drain cleaning for homes. Fast response, clean work and fair pricing on every job we take.</p><span class="btn">READ MORE</span></div>
  <div class="card"><div class="ph" role="img" aria-label="Commercial plumbing work"></div><h4>Commercial Services</h4><p>Hydrojetting, sewer line cleaning and water service repairs for offices, shops and restaurants with minimal downtime for your business.</p><span class="btn">READ MORE</span></div>
  <div class="card"><div class="ph" role="img" aria-label="Industrial plumbing work"></div><h4>Industrial Services</h4><p>Underground leak location with acoustic, thermal and tracer gas tools, plus large line cleaning and reroutes for industrial sites.</p><span class="btn">READ MORE</span></div>
</section>

<div class="abs video" role="img" aria-label="Blurred job site backdrop"></div>
<div class="abs player" role="img" aria-label="Video of hydrojetting equipment in use"></div>
<div class="abs bar"></div>
<svg class="abs" style="left:392px;top:1163px" width="16" height="16" viewBox="0 0 16 16"><path d="M3 2l11 6-11 6z" fill="#fff"/></svg>
<div class="abs" style="left:420px;top:1170px;width:380px;height:3px;background:#888"></div>
<div class="abs arrow" style="left:300px">&#8249;</div>
<div class="abs arrow" style="left:876px">&#8250;</div>

<div class="abs about-ph" role="img" aria-label="Company service vans parked outside"></div>
<section class="abs about">
  <h2>ABOUT US</h2>
  <p>We are full service plumbing contractors ready for any job, from drain cleaning and repairs to new construction. Our focus is leak detection under slabs and underground, with repairs and reroutes done right. We clean the whole pipe with high pressure hydrojetters and chain knocker cables that expand to fit the line.</p>
  <span class="btn">READ MORE</span>
</section>

<section class="abs testi"><h2>TESTIMONIAL</h2><div class="sub">What our customers say</div></section>
<div class="abs round" style="left:262px">&#8249;</div>
<div class="abs round" style="left:912px">&#8250;</div>
<div class="abs quote" style="left:300px">They found the slab leak in an hour without tearing up the floor. The crew was tidy, polite and explained every step of the repair to us.</div>
<div class="abs quote" style="left:630px">Our main drain kept backing up until they jetted the line. It has run clear ever since. Honest pricing and great service from start to finish.</div>
<div class="abs avatar" style="left:407px" role="img" aria-label="Customer portrait"></div>
<div class="abs avatar" style="left:737px" role="img" aria-label="Customer portrait"></div>
<div class="abs who" style="left:335px">Mark Ellison<span>Homeowner</span></div>
<div class="abs who" style="left:665px">Dana Ruiz<span>Business Owner</span></div>

<div class="abs cta"><span class="btn">REQUEST APPOINTMENT</span></div>
<div class="abs figure" role="img" aria-label="Plumber in uniform, shown from behind"></div>
<div class="abs cta-text">Schedule a Service with CLEARFLOW Today! Call 555.014.2290</div>

<footer class="abs footer"></footer>
<div class="abs fcol" style="left:268px"><h5>NAVIGATION</h5>Home<br>Services<br>About Us<br>Locations<br>Blog<br>Contact Us</div>
<div class="abs fcol" style="left:496px"><h5>OUR SERVICES</h5>Residential<br>Commercial<br>Industrial<br>Leak Detection<br>Drain Cleaning</div>
<div class="abs fcol" style="left:724px"><h5>CONTACT US</h5>ClearFlow Plumbing<br>100 Sample Road<br>Springfield, ST 00000<br>info@clearflowplumb.com<br>555.014.2290</div>
<div class="abs copy">Copyright © 2024 clearflowplumb.com</div>
</body>
</html>
```